Tomas Whitlow Design, LLC (www.tomaswhitlow.design)

A very hip, trendy architectural home page. Simple Menu upper right hand corner (About, Projects, Inspiration, Design-Build, Contact). In the "Projects" ... I want to click on each project and that will open up multiple photo's of that project. Attached are the graphics of my logo. I want the home page to be incredible ... I really market my name "Tomas Whitlow" as sophisticated architecture. Colors/branding should be black/metallic/white/grey maybe with a pop of a bright color but not much. My architecture is like www.brennerfaulkatelier.com if you want to review as example. My specialty is industrial design, homes with architectural concrete design, steel beams, alot of glass. Very modern. My work is best illustrated at www.vasquerlind.com.
Updates

Please see images uploaded in my brief. A new business card design by an AWESOME designer and some inspirational architectural projects I worked on.

Industry/Entity Type

Architecture

Coding

Coded - Design and coding required

Number of Pages Required

5+ page

Colors

Designer to choose only greyscale colors for use in the design.

Requirements
Must have
• The 1st project photo gallery is called "Raw Dwelling at Cypress Point"... Images of this project can be taken from: https://www.homeplotra.com/homedetails/2817-9th-St-SE-Naples-FL-34117/508164229_zpid/

The 2nd project photo gallery is called "Stone, Iron and Timber Residence at Cypress Point". I will upload images for this project but use placeholder until I finalize.

The 3rd photo gallery is called "Early Sketches: Off the Page". I will forward pictures. for this.

Website should be easy to update and handover at completion as we will be updating frequently. Wordpress, WIX, or other type is fine as long as it looks profesional and high-class.
Nice to have
• Maybe the home page loads to just "Tomas Whitlow Design, LLC ... Atelier for Bold Structural Vision" and has a click to enter button. Something cool maybe a fade it or something eye-catching and cool.
Should not have
• Should not be overly colorful.

```html
<!DOCTYPE html>
<html lang="en">
<head>
<meta charset="utf-8">
<title>Tomas Whitlow Design, LLC</title>
<link rel="stylesheet" href="https://fonts.googleapis.com/css2?family=Open+Sans:ital,wght@0,300;0,400;0,600;1,600&display=swap">
<style>
  :root {
    --bg-deep: #050505;
    --bg-lift: #1c1c1c;
    --text-dim: #6e6e6e;
    --text-soft: #c9c9c9;
    --text-bright: #e6e6e6;
    --rule: #8a8a8a;
    --frame: #d8d8d8;
  }
  * { margin: 0; padding: 0; box-sizing: border-box; }
  html, body {
    width: 1200px;
    height: 661px;
    overflow: hidden;
    background: var(--bg-deep);
  }
  .splash {
    position: relative;
    width: 1200px;
    height: 661px;
    font-family: "Open Sans", Arial, sans-serif;
    background:
      repeating-linear-gradient(0deg, rgba(255,255,255,0.012) 0 1px, transparent 1px 3px),
      radial-gradient(ellipse 60% 55% at 50% 45%, var(--bg-lift) 0%, #0d0d0d 55%, var(--bg-deep) 100%);
  }
  .welcome {
    position: absolute;
    top: 120px;
    left: 0;
    width: 1318px;
    text-align: center;
    font-size: 12px;
    letter-spacing: 2.6px;
    color: var(--text-dim);
    font-weight: 600;
  }
  .brand-square {
    position: absolute;
    left: 262px;
    top: 222px;
    width: 120px;
    height: 126px;
    border: 3px solid var(--text-soft);
  }
  .brand-rule {
    position: absolute;
    left: 410px;
    top: 172px;
    width: 3px;
    height: 228px;
    background: var(--rule);
  }
  .brand-name {
    position: absolute;
    left: 450px;
    top: 250px;
    width: 500px;
    text-align: center;
    font-size: 38px;
    font-weight: 300;
    letter-spacing: 1px;
    color: var(--text-bright);
    white-space: nowrap;
  }
  .tagline {
    position: absolute;
    top: 402px;
    left: 440px;
    width: 500px;
    text-align: center;
    font-size: 21px;
    font-style: italic;
    font-weight: 600;
    letter-spacing: 0.6px;
    color: var(--text-soft);
  }
  .enter-label {
    position: absolute;
    top: 465px;
    left: 0;
    width: 1342px;
    text-align: center;
    font-size: 12px;
    letter-spacing: 2.6px;
    color: var(--text-dim);
    font-weight: 600;
  }
  .enter-button {
    position: absolute;
    left: 630px;
    top: 516px;
    width: 83px;
    height: 42px;
    border: 2px solid var(--frame);
    display: flex;
    align-items: center;
    justify-content: center;
    text-decoration: none;
  }
</style>
</head>
<body>
  <main class="splash">
    <p class="welcome">WELCOME TO</p>
    <div class="brand-square"></div>
    <div class="brand-rule"></div>
    <h1 class="brand-name">Tomas Whitlow Design, LLC</h1>
    <p class="tagline">Atelier for Bold Structural Vision</p>
    <p class="enter-label">ENTER THE SITE</p>
    <a class="enter-button" href="#" aria-label="Enter the site">
      <svg width="26" height="14" viewBox="0 0 26 14" aria-hidden="true">
        <line x1="1" y1="7" x2="23" y2="7" stroke="#e6e6e6" stroke-width="2"/>
        <polyline points="16,1 23,7 16,13" fill="none" stroke="#e6e6e6" stroke-width="2"/>
      </svg>
    </a>
  </main>
</body>
</html>
```